Mental Health Awareness License Plates

Below is the sample format I will need. That of a plain license plate w/o frame
*refer to image with name Licence wo Frame*
Delete Frame
Replace QR Code with “MO”
Replace 2025 sticker with “ YR
Use License Plate font (attached)
On Ribbon, keep the green background
The California front leg, needs to be gradated like a sunset and retain shape of CA
Palm trees sharpened
I need the files in a format that can be used on a website, printed or made into a poster.
One file that reads SAMPLE, one version that reads “NEWPLA8”d
The finished product should look like a license plate as shown in the example
*refer to image name finished product*
I want to clarify what we are looking for. The license plate design has been approved by the state, but we need a high res version of it in multiple file formats. The most important change we are looking for is to the ribbon. The palm trees against the sunset are fuzzy, we need those placed in front of an sunset on the front leg of the ribbon. The rear leg needs to remain green (mental health color). I hope this help clarify our design need.

```html
<!DOCTYPE html>
<html lang="en">
<head>
<meta charset="utf-8">
<title>Mental Health Awareness License Plates</title>
<link rel="stylesheet" href="https://fonts.googleapis.com/css2?family=Kaushan+Script&family=Oswald:wght@400;700&family=Fira+Sans:ital,wght@1,600&display=swap">
<style>
  :root {
    --backdrop: #c1c2c4;
    --plate-edge: #ffffff;
    --plate-yellow: #fbea2c;
    --plate-aqua: #b9e2df;
    --script-red: #ee3a43;
    --number-black: #000000;
    --number-navy: #1d4b6b;
    --emblem-yellow-slot: #e6d52a;
    --emblem-aqua-slot: #a6d0cd;
  }
  html, body {
    margin: 0;
    padding: 0;
    width: 1200px;
    height: 1052px;
    overflow: hidden;
    background: var(--backdrop);
  }
  .canvas { display: block; width: 1200px; height: 1052px; }
  .plate-edge { fill: var(--plate-edge); }
  .plate-face--yellow { fill: var(--plate-yellow); }
  .plate-face--aqua { fill: var(--plate-aqua); }
  .mount-hole { fill: var(--plate-edge); }
  .emblem-slot--yellow { fill: var(--emblem-yellow-slot); }
  .emblem-slot--aqua { fill: var(--emblem-aqua-slot); }
  .state-name {
    font-family: "Kaushan Script", cursive;
    font-size: 84px;
    fill: var(--script-red);
  }
  .plate-number {
    font-family: "Oswald", sans-serif;
    font-weight: 400;
    font-size: 214px;
  }
  .plate-number--black { fill: var(--number-black); }
  .plate-number--navy { fill: var(--number-navy); }
  .cause-line {
    fill: var(--script-red);
    font-size: 25px;
  }
  .cause-line--bold { font-family: "Oswald", sans-serif; font-weight: 700; }
  .cause-line--italic { font-family: "Fira Sans", sans-serif; font-style: italic; font-weight: 600; }
</style>
</head>
<body>
<svg class="canvas" viewBox="0 0 1200 1052" xmlns="http://www.w3.org/2000/svg">

  <g class="plate plate--yellow">
    <rect class="plate-edge" x="194" y="93" width="765" height="382" rx="34"/>
    <rect class="plate-face--yellow" x="211" y="110" width="731" height="348" rx="18"/>
    <circle class="mount-hole" cx="355" cy="134" r="9"/>
    <circle class="mount-hole" cx="799" cy="134" r="9"/>
    <circle class="mount-hole" cx="355" cy="436" r="9"/>
    <circle class="mount-hole" cx="799" cy="436" r="9"/>
    <text class="state-name" x="575" y="192" text-anchor="middle" textLength="405" lengthAdjust="spacingAndGlyphs">California</text>
    <rect class="emblem-slot--yellow" x="237" y="230" width="102" height="181" rx="14" role="img" aria-label="Cause emblem artwork"/>
    <text class="plate-number plate-number--black" x="367" y="414" textLength="555" lengthAdjust="spacingAndGlyphs">CASURF</text>
    <text class="cause-line cause-line--bold" x="389" y="450" textLength="375" lengthAdjust="spacingAndGlyphs">MENTAL HEALTH AWARENESS</text>
  </g>

  <g class="plate plate--aqua" transform="translate(0 496)">
    <rect class="plate-edge" x="194" y="93" width="765" height="382" rx="34"/>
    <rect class="plate-face--aqua" x="211" y="110" width="731" height="348" rx="18"/>
    <circle class="mount-hole" cx="355" cy="134" r="9"/>
    <circle class="mount-hole" cx="799" cy="134" r="9"/>
    <circle class="mount-hole" cx="355" cy="436" r="9"/>
    <circle class="mount-hole" cx="799" cy="436" r="9"/>
    <text class="state-name" x="575" y="192" text-anchor="middle" textLength="405" lengthAdjust="spacingAndGlyphs">California</text>
    <rect class="emblem-slot--aqua" x="237" y="230" width="102" height="181" rx="14" role="img" aria-label="Cause emblem artwork"/>
    <text class="plate-number plate-number--navy" x="367" y="414" textLength="555" lengthAdjust="spacingAndGlyphs">CASURF</text>
    <text class="cause-line cause-line--italic" x="384" y="447" textLength="387" lengthAdjust="spacingAndGlyphs">MENTAL HEALTH AWARENESS</text>
  </g>
</svg>
</body>
</html>
```